Website Design for Forklift Training Company

DO NOT CONTACT PRIVATELY. ONLY SUBMISSIONS HERE WILL BE CONSIDERED

I need a design for a website that offers forklift training courses.

The company offers accredited, onsite forklift training that are customized for the needs of each individual company. The company offers a variety of courses to operate forklifts and other machinary.

About: "Pembrook Lift Academy Ltd delivers bespoke onsite forklift truck operator training throught the uk.
All our instructors have a wealth of knowledge and expertise to provide your company with all your forklift truck training requirements.
Pembrook Lift Academy Ltd is registered and accredited by qkmvd standards so you can be rest assured that all forklift training is carried out the very highest standard"

I need the following pages designed:
> a) Home Page: Include a header image, ways to contact, about snippet, overview of courses, accreditation that will be received after completing the courses. (See attachments for samples)
> b) About Page
> c) Contact Us Page
> d) Course Page Template: A page that will be used as template for the courses offered. It should contain;
1. Cover image for the course
2. A description of the course
3. A table indicating the various course options
4. Course Objectives
5. What the trainee will receive after doing the course (example: a certification)

Target Market(s)

Industrial Businesses

Number of Pages Required

4 page

Colors
0054AA
0677BA
7BADD7
CADEEF
E8F1F8
0094D4
00A9DD
6FCCEA
C7EBF8
E9F6FB

Requirements
Should not have
• - No Search bar

```html
<!DOCTYPE html>
<html lang="en">
<head>
<meta charset="utf-8">
<title>Forklift Training Website – Design Board</title>
<link rel="stylesheet" href="https://fonts.googleapis.com/css2?family=Bebas+Neue&family=Montserrat:wght@300;400&family=Poppins:ital,wght@0,400;0,600;0,700;0,800;1,800&display=swap">
<style>
  :root{
    --blue:#0054aa;
    --sky:#7badd7;
    --ice:#e3edf6;
    --board:#e7e7e7;
    --ink:#111;
    --text:#4a4a4a;
    --white:#fff;
    --black:#000;
  }
  *{box-sizing:border-box;margin:0;padding:0}
  html,body{width:1200px;height:900px;overflow:hidden;background:var(--board)}
  .board{position:relative;width:1200px;height:900px;overflow:hidden;background:var(--board);font-family:"Poppins",sans-serif}
  .abs{position:absolute}

  /* board labels */
  .board-title{position:absolute;font-family:"Poppins",sans-serif;font-weight:800;font-style:italic;font-size:16.5px;color:var(--ink);transform:translateX(-50%);white-space:nowrap;letter-spacing:.3px}
  .swatch{position:absolute;width:120px;height:103px;display:flex;align-items:center;justify-content:center;font-family:"Poppins",sans-serif;font-style:italic;font-size:11px;color:var(--white)}
  .swatch--primary{background:var(--blue)}
  .swatch--secondary{background:var(--sky)}
  .font-card{position:absolute;width:120px;height:103px;background:var(--white);display:flex;align-items:center;justify-content:center;color:var(--ink)}
  .font-card--display{font-family:"Bebas Neue",sans-serif;font-size:17px}
  .font-card--body{font-family:"Montserrat",sans-serif;font-size:11px}
  .button-label{position:absolute;left:340px;top:388px;transform:translateX(-50%);font-family:"Montserrat",sans-serif;font-weight:300;font-size:12px;letter-spacing:.6px;color:var(--ink);white-space:nowrap}
  .sample-btn{position:absolute;top:412px;width:104px;height:36px;display:flex;align-items:center;justify-content:center;font-family:"Montserrat",sans-serif;font-weight:300;font-size:8.5px;letter-spacing:.6px;color:var(--white)}
  .sample-btn--normal{left:234px;background:var(--blue)}
  .sample-btn--hover{left:343px;background:var(--black)}

  /* mockups */
  .mock{position:absolute;overflow:hidden;background:var(--white)}
  .mock--desktop{left:480px;top:66px;width:245px;height:784px}
  .mock--tablet{left:737px;top:66px;width:162px;height:606px}
  .mock--mobile{left:915px;top:66px;width:68px;height:822px}

  .hero-bg{position:absolute;left:0;top:0;width:100%;background:linear-gradient(160deg,#1d5fae,#0a4596)}
  .band{position:absolute;left:0;width:100%;background:var(--sky)}
  .courses-bg{position:absolute;left:0;width:100%;background:linear-gradient(180deg,#e6eef7,#dbe7f3 60%,#e8f0f8)}
  .contact-bg{position:absolute;left:0;width:100%;background:#f7f9fb}
  .footer{position:absolute;left:0;width:100%;background:var(--blue)}
  .copy-bar{position:absolute;left:0;width:100%;background:var(--black);color:#bbb;display:flex;align-items:center;justify-content:center;white-space:nowrap}

  .logo{position:absolute;display:flex;align-items:center;color:var(--white);font-family:"Poppins",sans-serif;font-weight:700;white-space:nowrap;line-height:1}
  .logo-mark{display:block;background:var(--white)}

  .nav{position:absolute;display:flex;color:var(--white);font-family:"Poppins",sans-serif;font-size:2.6px;letter-spacing:.3px;white-space:nowrap}
  .nav .is-active{text-decoration:underline}
  .burger{position:absolute;display:flex;flex-direction:column;justify-content:space-between}
  .burger span{display:block;height:.6px;background:var(--white)}

  .hero-title{position:absolute;font-family:"Poppins",sans-serif;font-weight:800;color:var(--white);text-transform:uppercase;line-height:.95;white-space:nowrap}
  .hero-text{position:absolute;font-family:"Poppins",sans-serif;color:#dfe8f4;overflow:hidden}

  .btn{position:absolute;display:flex;align-items:center;justify-content:center;font-family:"Poppins",sans-serif;color:var(--white);background:var(--blue);white-space:nowrap}
  .btn--dark{background:var(--black)}

  .feature{position:absolute;display:flex;flex-direction:column;align-items:center;color:var(--white);font-family:"Poppins",sans-serif;font-weight:600;white-space:nowrap;text-transform:uppercase}
  .feature svg{display:block}

  .section-title{position:absolute;display:flex;align-items:center;font-family:"Bebas Neue",sans-serif;color:var(--blue);white-space:nowrap;line-height:1}
  .section-title::after{content:"";display:block;border-top:.6px solid var(--blue);margin-left:2px}
  .course-title{position:absolute;font-family:"Bebas Neue",sans-serif;color:var(--blue);white-space:nowrap;line-height:1}
  .subtitle{position:absolute;font-family:"Poppins",sans-serif;color:var(--sky);white-space:nowrap}
  .copy{position:absolute;font-family:"Poppins",sans-serif;color:var(--text);overflow:hidden}

  .photo{position:absolute}
  .photo--framed{border:1px solid var(--blue);box-shadow:1.5px 1.5px 0 var(--blue)}
  .photo--warehouse{background:linear-gradient(135deg,#3a4656,#6b6a63 55%,#b08a3a)}
  .photo--about{background:linear-gradient(150deg,#5a5f66,#2f3a2e 50%,#a9a13b)}
  .photo--trainer{background:linear-gradient(135deg,#7f8c99,#b23a32 55%,#e8e4dc)}
  .photo--mewp{background:linear-gradient(180deg,#8fbfe9,#cfe3f3 45%,#e3c339 70%,#5f8f4a)}
  .photo--depot{background:linear-gradient(135deg,#6d5f4a,#c8763a 50%,#8c8f92)}
  .photo--truck-white{background:linear-gradient(180deg,#f4f5f6,#c9ccd0 55%,#e8c53a)}
  .photo--truck-blue{background:linear-gradient(180deg,#2a66b4,#7a8794 55%,#e0bd34)}
  .photo-outline{position:absolute;border:1px solid #c9c9c9;background:var(--white)}

  .contact-card{position:absolute;background:var(--blue)}
  .field{position:absolute;background:var(--sky);color:var(--white);font-family:"Poppins",sans-serif;text-transform:uppercase;white-space:nowrap;overflow:hidden}
  .captcha{position:absolute;background:var(--white);border:.4px solid #ccc;display:flex;align-items:center;font-family:"Poppins",sans-serif;color:#333;white-space:nowrap}
  .captcha i{display:block;border:.4px solid #888;background:var(--white)}

  .foot-head{position:absolute;font-family:"Bebas Neue",sans-serif;color:var(--white);white-space:nowrap;line-height:1}
  .foot-list{position:absolute;list-style:none;font-family:"Poppins",sans-serif;color:var(--white);white-space:nowrap}
  .foot-list li{display:flex;align-items:center}
  .foot-list svg{display:block;flex:none}
  .foot-text{position:absolute;font-family:"Poppins",sans-serif;color:#e1eaf6;overflow:hidden}
</style>
</head>
<body>
<svg width="0" height="0" style="position:absolute" aria-hidden="true">
  <defs>
    <symbol id="ic-bulb" viewBox="0 0 24 24"><circle cx="12" cy="10" r="6" fill="none" stroke="#fff" stroke-width="1.6"/><path d="M9 17h6M10 20h4M12 1v2M3 10h2M19 10h2M5 4l1.4 1.4M19 4l-1.4 1.4" stroke="#fff" stroke-width="1.6" fill="none"/></symbol>
    <symbol id="ic-badge" viewBox="0 0 24 24"><circle cx="12" cy="12" r="9" fill="none" stroke="#fff" stroke-width="1.8" stroke-dasharray="3 1.5"/><circle cx="12" cy="12" r="6" fill="none" stroke="#fff" stroke-width="1.4"/><path d="M9 12l2 2 4-4" stroke="#fff" stroke-width="1.6" fill="none"/></symbol>
    <symbol id="ic-user" viewBox="0 0 24 24"><circle cx="12" cy="7" r="4.5" fill="#fff"/><path d="M4 22c0-5 3.5-8 8-8s8 3 8 8z" fill="#fff"/></symbol>
    <symbol id="ic-headset" viewBox="0 0 24 24"><path d="M4 13a8 8 0 0 1 16 0" stroke="#fff" stroke-width="1.8" fill="none"/><rect x="3" y="12" width="4" height="6" rx="1.5" fill="#fff"/><rect x="17" y="12" width="4" height="6" rx="1.5" fill="#fff"/><path d="M19 18c0 2-2 3-5 3" stroke="#fff" stroke-width="1.4" fill="none"/></symbol>
    <symbol id="ic-pin" viewBox="0 0 24 24"><path d="M12 22s7-7 7-12a7 7 0 0 0-14 0c0 5 7 12 7 12z" fill="none" stroke="#fff" stroke-width="2"/><circle cx="12" cy="10" r="2.5" fill="#fff"/></symbol>
    <symbol id="ic-phone" viewBox="0 0 24 24"><path d="M5 3h4l2 5-3 2a12 12 0 0 0 6 6l2-3 5 2v4a2 2 0 0 1-2 2A18 18 0 0 1 3 5a2 2 0 0 1 2-2z" fill="none" stroke="#fff" stroke-width="2"/></symbol>
    <symbol id="ic-mail" viewBox="0 0 24 24"><rect x="3" y="5" width="18" height="14" fill="none" stroke="#fff" stroke-width="2"/><path d="M3 6l9 7 9-7" fill="none" stroke="#fff" stroke-width="2"/></symbol>
    <symbol id="ic-chev" viewBox="0 0 24 24"><path d="M8 5l8 7-8 7" fill="none" stroke="#fff" stroke-width="3"/></symbol>
  </defs>
</svg>

<main class="board">
  <!-- style guide -->
  <h2 class="board-title" style="left:348px;top:31px">Color Pallete</h2>
  <div class="swatch swatch--primary" style="left:217px;top:66px">#0054aa</div>
  <div class="swatch swatch--secondary" style="left:343px;top:66px">#7badd7</div>

  <h2 class="board-title" style="left:340px;top:208px">Font</h2>
  <div class="font-card font-card--display" style="left:217px;top:241px">BEBAS NEUE</div>
  <div class="font-card font-card--body" style="left:343px;top:241px">Montserrat</div>

  <p class="button-label">BUTTON ACTIONS OPTIONS</p>
  <div class="sample-btn sample-btn--normal">NORMAL</div>
  <div class="sample-btn sample-btn--hover">HOVER</div>

  <h2 class="board-title" style="left:603px;top:31px">Desktop</h2>
  <h2 class="board-title" style="left:818px;top:31px">Tablet</h2>
  <h2 class="board-title" style="left:949px;top:35px">Mobile</h2>

  <!-- ===== DESKTOP ===== -->
  <section class="mock mock--desktop" aria-label="Desktop home page">
    <div class="hero-bg" style="height:125px"></div>
    <svg class="abs" style="left:0;top:0" width="245" height="125" role="img" aria-label="Photo of a yellow forklift truck in a warehouse">
      <defs><linearGradient id="d-hero" x1="0" y1="0" x2="1" y2="1"><stop offset="0" stop-color="#3c4a5c"/><stop offset=".55" stop-color="#5d5a52"/><stop offset="1" stop-color="#2b2f36"/></linearGradient></defs>
      <polygon points="128,0 245,0 245,125 70,125" fill="url(#d-hero)"/>
    </svg>
    <div class="logo" style="left:27px;top:5px;font-size:6.5px"><span class="logo-mark" style="width:5px;height:5px;margin-right:1.5px"></span>LIFTPOINT</div>
    <nav class="nav" style="left:137px;top:6.5px;gap:6px"><span class="is-active">HOME</span><span>ABOUT US</span><span>COURSE</span><span>CONTACT US</span></nav>
    <h1 class="hero-title" style="left:27px;top:48px;font-size:9.4px">Build Your<br>Future Project</h1>
    <p class="hero-text" style="left:27px;top:69px;width:76px;height:13px;font-size:2.6px;line-height:4.3px">Lorem ipsum dolor sit amet, consectetur adipiscing elit, sed do eiusmod tempor incididunt ut labore et dolore magna aliqua.</p>
    <div class="btn btn--dark" style="left:27px;top:88px;width:29px;height:8px;font-size:2.4px">Contact Us</div>

    <div class="band" style="top:125px;height:28px"></div>
    <div class="feature" style="left:23px;top:131px;width:40px;font-size:2.8px"><svg width="12" height="12"><use href="#ic-bulb"/></svg><span style="margin-top:2px">Modern Technics</span></div>
    <div class="feature" style="left:78px;top:131px;width:40px;font-size:2.8px"><svg width="12" height="12"><use href="#ic-badge"/></svg><span style="margin-top:2px">Quality Materials</span></div>
    <div class="feature" style="left:134px;top:131px;width:40px;font-size:2.8px"><svg width="12" height="12"><use href="#ic-user"/></svg><span style="margin-top:2px">Professional Team</span></div>
    <div class="feature" style="left:186px;top:131px;width:40px;font-size:2.8px"><svg width="12" height="12"><use href="#ic-headset"/></svg><span style="margin-top:2px">24/7 Support</span></div>

    <div class="photo-outline" style="left:27px;top:167px;width:75px;height:81px"></div>
    <div class="photo photo--about" style="left:39px;top:177px;width:81px;height:82px" role="img" aria-label="Photo of instructors beside a forklift at a loading door"></div>
    <h2 class="section-title" style="left:126px;top:180px;font-size:7.5px">About Us<span></span></h2>
    <p class="subtitle" style="left:126px;top:187px;font-size:2.6px">We Are Here to Increase Your Knowledge With Experience</p>
    <p class="copy" style="left:126px;top:194px;width:94px;height:40px;font-size:2.5px;line-height:4.85px">"Pembrook Lift Academy Ltd delivers bespoke onsite forklift truck operator training throughout the UK.<br>All our instructors have a wealth of knowledge and expertise to provide your company with all your forklift truck training requirements.<br>Pembrook Lift Academy Ltd is registered and accredited by qkmvd standards so you can rest assured that all forklift training is carried out to the very highest standard"</p>
    <div class="btn" style="left:126px;top:238px;width:30px;height:8px;font-size:2.5px">Know More</div>

    <div class="courses-bg" style="top:272px;height:280px" role="img" aria-label="Faint warehouse photo behind the courses section"></div>
    <h2 class="section-title" style="left:27px;top:286px;font-size:7.5px">Our Courses</h2>
    <p class="copy" style="left:27px;top:296px;width:185px;height:9px;font-size:2.6px;line-height:4.4px">Lorem ipsum dolor sit amet, consectetur adipiscing elit, sed do eiusmod tempor incididunt ut labore et dolore magna aliqua.</p>

    <div class="photo photo--framed photo--trainer" style="left:27px;top:310px;width:93px;height:73px" role="img" aria-label="Photo of an instructor showing a trainee forklift controls"></div>
    <h3 class="course-title" style="left:126px;top:320px;font-size:7px">Forklift Training Course</h3>
    <p class="copy" style="left:126px;top:330px;width:93px;height:28px;font-size:2.5px;line-height:4.85px">Lorem Ipsum is simply dummy text of the printing and typesetting industry. Lorem Ipsum has been the industry's standard dummy text ever since the 1500s, when an unknown printer took a galley of type and scrambled it to make a type specimen book. It has survived not only five centuries, but also the leap into electronic typesetting, remaining essentially unchanged.</p>
    <div class="btn" style="left:126px;top:365px;width:29px;height:7px;font-size:2.4px">Know More</div>

    <h3 class="course-title" style="left:27px;top:399px;font-size:7px">MEWP Training Course</h3>
    <p class="copy" style="left:27px;top:409px;width:93px;height:28px;font-size:2.5px;line-height:4.85px">Lorem Ipsum is simply dummy text of the printing and typesetting industry. Lorem Ipsum has been the industry's standard dummy text ever since the 1500s, when an unknown printer took a galley of type and scrambled it to make a type specimen book. It has survived not only five centuries, but also the leap into electronic typesetting, remaining essentially unchanged.</p>
    <div class="btn" style="left:27px;top:444px;width:29px;height:7px;font-size:2.4px">Know More</div>
    <div class="photo photo--framed photo--mewp" style="left:126px;top:388px;width:93px;height:74px" role="img" aria-label="Photo of a yellow scissor lift under a blue sky"></div>

    <div class="photo photo--framed photo--depot" style="left:27px;top:467px;width:93px;height:73px" role="img" aria-label="Photo of workers in hi-vis vests beside a forklift in a depot"></div>
    <h3 class="course-title" style="left:126px;top:478px;font-size:7px">Other Training Course</h3>
    <p class="copy" style="left:126px;top:488px;width:93px;height:28px;font-size:2.5px;line-height:4.85px">Lorem Ipsum is simply dummy text of the printing and typesetting industry. Lorem Ipsum has been the industry's standard dummy text ever since the 1500s, when an unknown printer took a galley of type and scrambled it to make a type specimen book. It has survived not only five centuries, but also the leap into electronic typesetting, remaining essentially unchanged.</p>
    <div class="btn" style="left:126px;top:523px;width:29px;height:7px;font-size:2.4px">Know More</div>

    <div class="contact-bg" style="top:552px;height:133px"></div>
    <div class="contact-card" style="left:27px;top:566px;width:93px;height:106px;border-radius:12px 0 0 12px"></div>
    <h2 class="section-title" style="left:32px;top:576px;font-size:7px;color:#fff">Contact Us</h2>
    <div class="field" style="left:32px;top:587px;width:83px;height:7px;font-size:2px;padding:2.3px 2px">Name</div>
    <div class="field" style="left:32px;top:597px;width:83px;height:7px;font-size:2px;padding:2.3px 2px">Phone Number</div>
    <div class="field" style="left:32px;top:608px;width:83px;height:7px;font-size:2px;padding:2.3px 2px">Email</div>
    <div class="field" style="left:32px;top:617px;width:83px;height:20px;font-size:2px;padding:3px 2px">Message</div>
    <div class="captcha" style="left:32px;top:640px;width:49px;height:12px;font-size:2px;padding-left:2px;gap:2px"><i style="width:4px;height:4px"></i>I'm not a robot</div>
    <div class="btn btn--dark" style="left:32px;top:655px;width:45px;height:7px;font-size:2.2px">SUBMIT</div>
    <div class="photo photo--truck-white" style="left:125px;top:566px;width:92px;height:106px" role="img" aria-label="Photo of a grey and yellow electric forklift"></div>

    <div class="footer" style="top:685px;height:91px"></div>
    <div class="photo photo--truck-blue" style="left:29px;top:695px;width:69px;height:70px" role="img" aria-label="Photo of a yellow electric forklift"></div>
    <div class="logo" style="left:126px;top:701px;font-size:9.5px"><span class="logo-mark" style="width:7px;height:7px;margin-right:2px"></span>LIFTPOINT</div>
    <p class="foot-text" style="left:126px;top:716px;width:93px;height:19px;font-size:2.5px;line-height:4.4px">Lorem ipsum dolor sit amet, consectetur adipiscing elit, sed do eiusmod tempor incididunt ut labore et dolore magna aliqua. Quis ipsum suspendisse ultrices gravida. Risus commodo viverra maecenas accumsan lacus vel facilisis.</p>
    <h4 class="foot-head" style="left:126px;top:738px;font-size:4.4px">Important Links</h4>
    <ul class="foot-list" style="left:126px;top:745px;font-size:2.4px;line-height:4.7px">
      <li><svg width="2" height="2"><use href="#ic-chev"/></svg>&nbsp;&nbsp;Home</li>
      <li><svg width="2" height="2"><use href="#ic-chev"/></svg>&nbsp;&nbsp;About Us</li>
      <li><svg width="2" height="2"><use href="#ic-chev"/></svg>&nbsp;&nbsp;Our Courses</li>
      <li><svg width="2" height="2"><use href="#ic-chev"/></svg>&nbsp;&nbsp;Contact Us</li>
    </ul>
    <h4 class="foot-head" style="left:174px;top:738px;font-size:4.4px">Information</h4>
    <ul class="foot-list" style="left:174px;top:745px;font-size:2.4px;line-height:2.8px">
      <li><svg width="3" height="3"><use href="#ic-pin"/></svg>&nbsp;&nbsp;42 Kestrel Lane<br>&nbsp;&nbsp;Dunmore, USA</li>
      <li style="margin-top:1.5px"><svg width="3" height="3"><use href="#ic-phone"/></svg>&nbsp;&nbsp;+01-555-0148</li>
      <li style="margin-top:2px"><svg width="3" height="3"><use href="#ic-mail"/></svg>&nbsp;&nbsp;hello@liftpoint.example</li>
    </ul>
    <div class="copy-bar" style="top:776px;height:8px;font-size:2px">© 2021 LiftPoint. All rights reserved.</div>
  </section>

  <!-- ===== TABLET ===== -->
  <section class="mock mock--tablet" aria-label="Tablet home page">
    <div class="hero-bg" style="height:82px"></div>
    <svg class="abs" style="left:0;top:0" width="162" height="82" role="img" aria-label="Photo of a yellow forklift truck in a warehouse">
      <defs><linearGradient id="t-hero" x1="0" y1="0" x2="1" y2="1"><stop offset="0" stop-color="#3c4a5c"/><stop offset=".55" stop-color="#5d5a52"/><stop offset="1" stop-color="#2b2f36"/></linearGradient></defs>
      <polygon points="88,0 162,0 162,82 42,82" fill="url(#t-hero)"/>
    </svg>
    <div class="logo" style="left:5px;top:2.5px;font-size:4.6px"><span class="logo-mark" style="width:3.5px;height:3.5px;margin-right:1px"></span>LIFTPOINT</div>
    <div class="burger" style="left:151px;top:3px;width:5.5px;height:4px"><span></span><span></span><span></span></div>
    <h1 class="hero-title" style="left:5px;top:32px;font-size:6.3px">Build Your<br>Future Project</h1>
    <p class="hero-text" style="left:5px;top:46px;width:50px;height:10px;font-size:1.7px;line-height:2.9px">Lorem ipsum dolor sit amet, consectetur adipiscing elit, sed do eiusmod tempor incididunt ut labore et dolore magna aliqua.</p>
    <div class="btn btn--dark" style="left:5px;top:58px;width:15px;height:5px;font-size:1.6px">Contact Us</div>

    <div class="band" style="top:82px;height:19px"></div>
    <div class="feature" style="left:14px;top:84px;width:30px;font-size:1.6px"><svg width="8" height="8"><use href="#ic-bulb"/></svg><span style="margin-top:1.5px">Modern Technics</span></div>
    <div class="feature" style="left:50px;top:84px;width:30px;font-size:1.6px"><svg width="8" height="8"><use href="#ic-badge"/></svg><span style="margin-top:1.5px">Quality Materials</span></div>
    <div class="feature" style="left:87px;top:84px;width:30px;font-size:1.6px"><svg width="8" height="8"><use href="#ic-user"/></svg><span style="margin-top:1.5px">Professional Team</span></div>
    <div class="feature" style="left:121px;top:84px;width:30px;font-size:1.6px"><svg width="8" height="8"><use href="#ic-headset"/></svg><span style="margin-top:1.5px">24/7 Support</span></div>

    <div class="photo-outline" style="left:5px;top:111px;width:64px;height:66px"></div>
    <div class="photo photo--about" style="left:15px;top:119px;width:65px;height:66px" role="img" aria-label="Photo of instructors beside a forklift at a loading door"></div>
    <h2 class="section-title" style="left:83px;top:122px;font-size:5.3px">About Us</h2>
    <p class="subtitle" style="left:83px;top:127.5px;font-size:1.6px">We Are Here to Increase Your Knowledge With Experience</p>
    <p class="copy" style="left:83px;top:132px;width:74px;height:34px;font-size:1.65px;line-height:3.7px">"Pembrook Lift Academy Ltd delivers bespoke onsite forklift truck operator training throughout the UK.<br>All our instructors have a wealth of knowledge and expertise to provide your company with all your forklift truck training requirements.<br>Pembrook Lift Academy Ltd is registered and accredited by qkmvd standards so you can rest assured that all forklift training is carried out to the very highest standard"</p>
    <div class="btn" style="left:83px;top:168px;width:23px;height:5px;font-size:1.7px">Know More</div>

    <div class="courses-bg" style="top:195px;height:224px" role="img" aria-label="Faint warehouse photo behind the courses section"></div>
    <h2 class="section-title" style="left:5px;top:206px;font-size:5.3px">Our Courses</h2>
    <p class="copy" style="left:5px;top:213px;width:150px;height:6px;font-size:1.65px;line-height:3px">Lorem ipsum dolor sit amet, consectetur adipiscing elit, sed do eiusmod tempor incididunt ut labore et dolore magna aliqua.</p>

    <div class="photo photo--framed photo--trainer" style="left:5px;top:225px;width:75px;height:58px" role="img" aria-label="Photo of an instructor showing a trainee forklift controls"></div>
    <h3 class="course-title" style="left:83px;top:233px;font-size:5px">Forklift Training Course</h3>
    <p class="copy" style="left:83px;top:240px;width:74px;height:24px;font-size:1.65px;line-height:3.7px">Lorem Ipsum is simply dummy text of the printing and typesetting industry. Lorem Ipsum has been the industry's standard dummy text ever since the 1500s, when an unknown printer took a galley of type and scrambled it to make a type specimen book. It has survived not only five centuries, but also the leap into electronic typesetting, remaining essentially unchanged.</p>
    <div class="btn" style="left:83px;top:268px;width:18px;height:5px;font-size:1.5px">Know More</div>

    <h3 class="course-title" style="left:5px;top:296px;font-size:5px">MEWP Training Course</h3>
    <p class="copy" style="left:5px;top:303px;width:74px;height:24px;font-size:1.65px;line-height:3.7px">Lorem Ipsum is simply dummy text of the printing and typesetting industry. Lorem Ipsum has been the industry's standard dummy text ever since the 1500s, when an unknown printer took a galley of type and scrambled it to make a type specimen book. It has survived not only five centuries, but also the leap into electronic typesetting, remaining essentially unchanged.</p>
    <div class="btn" style="left:5px;top:331px;width:18px;height:5px;font-size:1.5px">Know More</div>
    <div class="photo photo--framed photo--mewp" style="left:83px;top:287px;width:74px;height:59px" role="img" aria-label="Photo of a yellow scissor lift under a blue sky"></div>

    <div class="photo photo--framed photo--depot" style="left:5px;top:350px;width:75px;height:58px" role="img" aria-label="Photo of workers in hi-vis vests beside a forklift in a depot"></div>
    <h3 class="course-title" style="left:83px;top:358px;font-size:5px">Other Training Course</h3>
    <p class="copy" style="left:83px;top:365px;width:74px;height:24px;font-size:1.65px;line-height:3.7px">Lorem Ipsum is simply dummy text of the printing and typesetting industry. Lorem Ipsum has been the industry's standard dummy text ever since the 1500s, when an unknown printer took a galley of type and scrambled it to make a type specimen book. It has survived not only five centuries, but also the leap into electronic typesetting, remaining essentially unchanged.</p>
    <div class="btn" style="left:83px;top:393px;width:18px;height:5px;font-size:1.5px">Know More</div>

    <div class="contact-bg" style="top:419px;height:107px"></div>
    <div class="contact-card" style="left:5px;top:428px;width:75px;height:85px;border-radius:10px 0 0 10px"></div>
    <h2 class="section-title" style="left:9px;top:437px;font-size:5px;color:#fff">Contact Us</h2>
    <div class="field" style="left:9px;top:444px;width:67px;height:6px;font-size:1.4px;padding:2px 1.5px">Name</div>
    <div class="field" style="left:9px;top:453px;width:67px;height:6px;font-size:1.4px;padding:2px 1.5px">Phone Number</div>
    <div class="field" style="left:9px;top:461px;width:67px;height:6px;font-size:1.4px;padding:2px 1.5px">Email</div>
    <div class="field" style="left:9px;top:470px;width:67px;height:14px;font-size:1.4px;padding:2px 1.5px">Message</div>
    <div class="captcha" style="left:9px;top:487px;width:40px;height:9px;font-size:1.4px;padding-left:1.5px;gap:1.5px"><i style="width:3px;height:3px"></i>I'm not a robot</div>
    <div class="btn btn--dark" style="left:9px;top:499.5px;width:36px;height:5px;font-size:1.5px">SUBMIT</div>
    <div class="photo photo--truck-white" style="left:83px;top:428px;width:74px;height:85px" role="img" aria-label="Photo of a grey and yellow electric forklift"></div>

    <div class="footer" style="top:526px;height:74px"></div>
    <div class="photo photo--truck-blue" style="left:5px;top:534px;width:56px;height:57px" role="img" aria-label="Photo of a yellow electric forklift"></div>
    <div class="logo" style="left:82px;top:538px;font-size:7px"><span class="logo-mark" style="width:5px;height:5px;margin-right:1.5px"></span>LIFTPOINT</div>
    <p class="foot-text" style="left:82px;top:550px;width:75px;height:14px;font-size:1.6px;line-height:3.3px">Lorem ipsum dolor sit amet, consectetur adipiscing elit, sed do eiusmod tempor incididunt ut labore et dolore magna aliqua. Quis ipsum suspendisse ultrices gravida. Risus commodo viverra maecenas accumsan lacus vel facilisis.</p>
    <h4 class="foot-head" style="left:82px;top:567px;font-size:3.3px">Important Links</h4>
    <ul class="foot-list" style="left:82px;top:573px;font-size:1.5px;line-height:3.6px">
      <li><svg width="1.5" height="1.5"><use href="#ic-chev"/></svg>&nbsp;&nbsp;Home</li>
      <li><svg width="1.5" height="1.5"><use href="#ic-chev"/></svg>&nbsp;&nbsp;About Us</li>
      <li><svg width="1.5" height="1.5"><use href="#ic-chev"/></svg>&nbsp;&nbsp;Our Courses</li>
      <li><svg width="1.5" height="1.5"><use href="#ic-chev"/></svg>&nbsp;&nbsp;Contact Us</li>
    </ul>
    <h4 class="foot-head" style="left:122px;top:567px;font-size:3.3px">Information</h4>
    <ul class="foot-list" style="left:122px;top:573px;font-size:1.5px;line-height:2px">
      <li><svg width="2.2" height="2.2"><use href="#ic-pin"/></svg>&nbsp;&nbsp;42 Kestrel Lane<br>&nbsp;&nbsp;Dunmore, USA</li>
      <li style="margin-top:1.2px"><svg width="2.2" height="2.2"><use href="#ic-phone"/></svg>&nbsp;&nbsp;+01-555-0148</li>
      <li style="margin-top:1.6px"><svg width="2.2" height="2.2"><use href="#ic-mail"/></svg>&nbsp;&nbsp;hello@liftpoint.example</li>
    </ul>
    <div class="copy-bar" style="top:600px;height:6px;font-size:1.4px">© 2021 LiftPoint. All rights reserved.</div>
  </section>

  <!-- ===== MOBILE ===== -->
  <section class="mock mock--mobile" aria-label="Mobile home page">
    <div class="hero-bg" style="height:74px" role="img" aria-label="Faint warehouse photo under a blue overlay"></div>
    <div class="logo" style="left:2px;top:2px;font-size:3px"><span class="logo-mark" style="width:2.4px;height:2.4px;margin-right:.7px"></span>LIFTPOINT</div>
    <div class="burger" style="left:62px;top:3px;width:3.5px;height:2.6px"><span style="height:.4px"></span><span style="height:.4px"></span><span style="height:.4px"></span></div>
    <h1 class="hero-title" style="left:3px;top:26px;font-size:5.5px">Build Your<br>Future Project</h1>
    <p class="hero-text" style="left:3px;top:39px;width:54px;height:8px;font-size:1.45px;line-height:2.5px">Lorem ipsum dolor sit amet, consectetur adipiscing elit, sed do eiusmod tempor incididunt ut labore et dolore magna aliqua.</p>
    <div class="btn btn--dark" style="left:3px;top:50.5px;width:10px;height:4px;font-size:1.1px">Contact Us</div>

    <div class="band" style="top:74px;height:37px"></div>
    <div class="feature" style="left:2px;top:80px;width:24px;font-size:1.2px"><svg width="6" height="6"><use href="#ic-bulb"/></svg><span style="margin-top:.8px">Modern Technics</span></div>
    <div class="feature" style="left:41px;top:80px;width:24px;font-size:1.2px"><svg width="6" height="6"><use href="#ic-user"/></svg><span style="margin-top:.8px">Professional Team</span></div>
    <div class="feature" style="left:2px;top:96px;width:24px;font-size:1.2px"><svg width="6" height="6"><use href="#ic-badge"/></svg><span style="margin-top:.8px">Quality Materials</span></div>
    <div class="feature" style="left:41px;top:96px;width:24px;font-size:1.2px"><svg width="6" height="6"><use href="#ic-headset"/></svg><span style="margin-top:.8px">24/7 Support</span></div>

    <div class="photo-outline" style="left:2px;top:116px;width:56px;height:58px"></div>
    <div class="photo photo--about" style="left:9px;top:122px;width:57px;height:59px" role="img" aria-label="Photo of instructors beside a forklift at a loading door"></div>
    <h2 class="section-title" style="left:2px;top:189px;font-size:4px">About Us</h2>
    <p class="subtitle" style="left:2px;top:193.5px;font-size:1.1px">We Are Here to Increase Your Knowledge With Experience</p>
    <p class="copy" style="left:2px;top:197px;width:63px;height:27px;font-size:1.15px;line-height:2.25px">"Pembrook Lift Academy Ltd delivers bespoke onsite forklift truck operator training throughout the UK.<br>All our instructors have a wealth of knowledge and expertise to provide your company with all your forklift truck training requirements.<br>Pembrook Lift Academy Ltd is registered and accredited by qkmvd standards so you can rest assured that all forklift training is carried out to the very highest standard"</p>
    <div class="btn" style="left:2px;top:229px;width:10px;height:3.5px;font-size:1px">Know More</div>

    <div class="courses-bg" style="top:241px;height:316px" role="img" aria-label="Faint warehouse photo behind the courses section"></div>
    <h2 class="section-title" style="left:2px;top:247px;font-size:4px">Our Courses</h2>
    <p class="copy" style="left:2px;top:254px;width:62px;height:10px;font-size:1.35px;line-height:2.4px">Lorem ipsum dolor sit amet, consectetur adipiscing elit, sed do eiusmod tempor incididunt ut labore et dolore magna aliqua.</p>

    <div class="photo photo--framed photo--trainer" style="left:2px;top:269px;width:63px;height:49px" role="img" aria-label="Photo of an instructor showing a trainee forklift controls"></div>
    <h3 class="course-title" style="left:2px;top:325px;font-size:4px">Forklift Training Course</h3>
    <p class="copy" style="left:2px;top:331px;width:63px;height:21px;font-size:1.15px;line-height:2.3px">Lorem Ipsum is simply dummy text of the printing and typesetting industry. Lorem Ipsum has been the industry's standard dummy text ever since the 1500s, when an unknown printer took a galley of type and scrambled it to make a type specimen book. It has survived not only five centuries, but also the leap into electronic typesetting, remaining essentially unchanged.</p>
    <div class="btn" style="left:2px;top:354.5px;width:10px;height:3.5px;font-size:1px">Know More</div>

    <div class="photo photo--framed photo--mewp" style="left:2px;top:366px;width:63px;height:49px" role="img" aria-label="Photo of a yellow scissor lift under a blue sky"></div>
    <h3 class="course-title" style="left:2px;top:420px;font-size:4px">MEWP Training Course</h3>
    <p class="copy" style="left:2px;top:426px;width:63px;height:21px;font-size:1.15px;line-height:2.3px">Lorem Ipsum is simply dummy text of the printing and typesetting industry. Lorem Ipsum has been the industry's standard dummy text ever since the 1500s, when an unknown printer took a galley of type and scrambled it to make a type specimen book. It has survived not only five centuries, but also the leap into electronic typesetting, remaining essentially unchanged.</p>
    <div class="btn" style="left:2px;top:449.5px;width:10px;height:3.5px;font-size:1px">Know More</div>

    <div class="photo photo--framed photo--depot" style="left:2px;top:460px;width:63px;height:49px" role="img" aria-label="Photo of workers in hi-vis vests beside a forklift in a depot"></div>
    <h3 class="course-title" style="left:2px;top:515px;font-size:4px">Other Training Course</h3>
    <p class="copy" style="left:2px;top:521px;width:63px;height:21px;font-size:1.15px;line-height:2.3px">Lorem Ipsum is simply dummy text of the printing and typesetting industry. Lorem Ipsum has been the industry's standard dummy text ever since the 1500s, when an unknown printer took a galley of type and scrambled it to make a type specimen book. It has survived not only five centuries, but also the leap into electronic typesetting, remaining essentially unchanged.</p>
    <div class="btn" style="left:2px;top:544.5px;width:10px;height:3.5px;font-size:1px">Know More</div>

    <div class="contact-bg" style="top:557px;height:162px"></div>
    <div class="contact-card" style="left:3px;top:564px;width:62px;height:71px"></div>
    <h2 class="section-title" style="left:6px;top:571px;font-size:3.8px;color:#fff">Contact Us</h2>
    <div class="field" style="left:6px;top:577px;width:56px;height:4px;font-size:1px;padding:1.3px 1px">Name</div>
    <div class="field" style="left:6px;top:584.5px;width:56px;height:4px;font-size:1px;padding:1.3px 1px">Phone Number</div>
    <div class="field" style="left:6px;top:591.5px;width:56px;height:4px;font-size:1px;padding:1.3px 1px">Email</div>
    <div class="field" style="left:6px;top:597px;width:56px;height:13px;font-size:1px;padding:1.5px 1px">Message</div>
    <div class="captcha" style="left:6px;top:613px;width:28px;height:7px;font-size:1px;padding-left:1px;gap:1px"><i style="width:2px;height:2px"></i>I'm not a robot</div>
    <div class="btn btn--dark" style="left:6px;top:623px;width:14px;height:4px;font-size:1px">SUBMIT</div>
    <div class="photo photo--truck-white" style="left:2px;top:639px;width:64px;height:76px" role="img" aria-label="Photo of a grey and yellow electric forklift"></div>

    <div class="footer" style="top:719px;height:95px"></div>
    <div class="logo" style="left:2px;top:731px;font-size:4.4px"><span class="logo-mark" style="width:3.2px;height:3.2px;margin-right:1px"></span>LIFTPOINT</div>
    <p class="foot-text" style="left:2px;top:740px;width:63px;height:18px;font-size:1.25px;line-height:2.4px">Lorem ipsum dolor sit amet, consectetur adipiscing elit, sed do eiusmod tempor incididunt ut labore et dolore magna aliqua. Quis ipsum suspendisse ultrices gravida. Risus commodo viverra maecenas accumsan lacus vel facilisis.</p>
    <h4 class="foot-head" style="left:2px;top:762.5px;font-size:2.8px">Information</h4>
    <ul class="foot-list" style="left:4px;top:767px;font-size:1.15px;line-height:1.6px">
      <li><svg width="1.8" height="1.8"><use href="#ic-pin"/></svg>&nbsp;&nbsp;42 Kestrel Lane<br>&nbsp;&nbsp;Dunmore, USA</li>
      <li style="margin-top:1px"><svg width="1.8" height="1.8"><use href="#ic-phone"/></svg>&nbsp;&nbsp;+01-555-0148</li>
      <li style="margin-top:1.5px"><svg width="1.8" height="1.8"><use href="#ic-mail"/></svg>&nbsp;&nbsp;hello@liftpoint.example</li>
    </ul>
    <h4 class="foot-head" style="left:2px;top:787.5px;font-size:2.8px">Important Links</h4>
    <ul class="foot-list" style="left:2px;top:792.5px;font-size:1.1px;line-height:3.3px">
      <li><svg width="1.2" height="1.2"><use href="#ic-chev"/></svg>&nbsp;&nbsp;Home</li>
      <li><svg width="1.2" height="1.2"><use href="#ic-chev"/></svg>&nbsp;&nbsp;About Us</li>
      <li><svg width="1.2" height="1.2"><use href="#ic-chev"/></svg>&nbsp;&nbsp;Our Courses</li>
      <li><svg width="1.2" height="1.2"><use href="#ic-chev"/></svg>&nbsp;&nbsp;Contact Us</li>
    </ul>
    <div class="copy-bar" style="top:814px;height:8px;font-size:1px">© 2021 LiftPoint. All rights reserved.</div>
  </section>
</main>
</body>
</html>
```